Custom Apparel Decorating Company needs a Website Home Page Banner Design

We are in need of a website Home page banner design for a small company based in Canada called Quelvana. We are a custom apparel company that offers custom apparel (t-shirts, hoodies, hats etc) to Companies, Organizations/groups, bands, Spirit wear and individuals. We would like the design to match with the logo files we have attached to the campaign. The Website has not been created yet planning to tie the website into the home page banner for flow. Thinking of using Duda or Shopify for the website if that helps! We are really looking forward to seeing the designs.

Target Market(s)

Companies, Organizations/Groups, Bands, Spirit wear and Individuals. Anyone that is looking to have there company or own logo/Design put on a piece of clothing.

Requirements
Must have
• -Colours in the logo files.
• -FUN creating the Home Page Banner!!! :)
Nice to have
• -Up Beat feel to it (it's the first image you will see when you go to the website, it's the store front so we want to grab the attention of the potential customers)

```html
<!DOCTYPE html>
<html lang="en">
<head>
<meta charset="UTF-8">
<title>Quelvana Apparel – Home Banner</title>
<link href="https://fonts.googleapis.com/css2?family=Michroma&display=swap" rel="stylesheet">
<style>
  :root {
    --brand-blue: #4a78c2;
    --ink: #1f1f1f;
    --grey-1: #3c3c3c;
    --grey-2: #5e5e5e;
    --grey-3: #858585;
    --grey-4: #acacac;
    --grey-5: #d2d2d2;
    --paper: #ffffff;
  }
  html, body {
    margin: 0;
    padding: 0;
    overflow: hidden;
    background: var(--paper);
  }
  .banner {
    position: relative;
    width: 1200px;
    height: 148px;
    overflow: hidden;
    background: var(--paper);
  }
  .banner__stripes {
    position: absolute;
    left: 0;
    top: 0;
  }
  .stripe--blue { fill: var(--brand-blue); }
  .stripe--ink { fill: var(--ink); }
  .stripe--g1 { fill: var(--grey-1); }
  .stripe--g2 { fill: var(--grey-2); }
  .stripe--g3 { fill: var(--grey-3); }
  .stripe--g4 { fill: var(--grey-4); }
  .stripe--g5 { fill: var(--grey-5); }

  .lockup {
    position: absolute;
    right: 40px;
    top: 0;
    width: 300px;
    height: 148px;
    display: flex;
    flex-direction: column;
    align-items: center;
    justify-content: center;
    gap: 18px;
  }
  .lockup__square {
    width: 40px;
    height: 40px;
    background: var(--brand-blue);
  }
  .lockup__name {
    margin: 0;
    font-family: "Michroma", sans-serif;
    font-weight: 400;
    font-size: 19px;
    letter-spacing: 0.5px;
    color: var(--brand-blue);
    white-space: nowrap;
  }
</style>
</head>
<body>
  <header class="banner">
    <svg class="banner__stripes" width="820" height="148" viewBox="0 0 820 148" aria-hidden="true">
      <!-- grey chevrons, lightest at the back -->
      <polygon class="stripe--g5" points="0,0 740,0 800,74 740,148 0,148"/>
      <polygon class="stripe--g4" points="0,0 690,0 750,74 690,148 0,148"/>
      <polygon class="stripe--g3" points="0,0 640,0 700,74 640,148 0,148"/>
      <polygon class="stripe--g2" points="0,0 595,0 655,74 595,148 0,148"/>
      <polygon class="stripe--g1" points="0,0 550,0 610,74 550,148 0,148"/>
      <polygon class="stripe--ink" points="0,0 505,0 565,74 505,148 0,148"/>
      <!-- solid blue block -->
      <polygon class="stripe--blue" points="0,0 450,0 510,74 450,148 0,148"/>
      <!-- fading blue layers -->
      <polygon fill="#ffffff" opacity="0.18" points="0,0 265,0 325,74 265,148 0,148"/>
      <polygon fill="#ffffff" opacity="0.15" points="0,0 225,0 285,74 225,148 0,148"/>
      <polygon fill="#ffffff" opacity="0.15" points="0,0 185,0 245,74 185,148 0,148"/>
      <polygon fill="#ffffff" opacity="0.15" points="0,0 145,0 205,74 145,148 0,148"/>
      <polygon fill="#ffffff" opacity="0.15" points="0,0 100,0 160,74 100,148 0,148"/>
      <polygon fill="#ffffff" opacity="0.15" points="0,0 50,0 110,74 50,148 0,148"/>
    </svg>

    <div class="lockup">
      <div class="lockup__square" aria-hidden="true"></div>
      <p class="lockup__name">QUELVANA Apparel</p>
    </div>
  </header>
</body>
</html>
```